Business Card Design Project

We need a business card design for a new construction company called 'KVORA HOLDINGS PTY.LTD' We run a construction based company for high end market homes in melbourne, we want something that looks professional and eye catching.The card needs to have a strong design to it something modern as the company name explains "kvora." The final design should communicate professionalism and a strong image to our customers on the quality of our work.
On the business card i need
Name: Marek Tollaway
Mob:0417295041
Email:kvora.holdings@mailbrook.example
Domestic/Residential/Commercial
Industry/Entity Type
Construction
Look and feel
Each slider illustrates characteristics of the customer's brand and the style your logo design should communicate.

```html
<!DOCTYPE html>
<html lang="en">
<head>
<meta charset="utf-8">
<title>Kvora Holdings – Business Card</title>
<link rel="stylesheet" href="https://fonts.googleapis.com/css2?family=Questrial&display=swap">
<style>
  :root {
    --backdrop: #3a3a3a;
    --card-black: #151515;
    --brand-red: #b3141d;
    --brand-red-dark: #8e0f16;
    --text-light: #f2f2f2;
    --text-muted: #d8d8d8;
  }
  * { box-sizing: border-box; margin: 0; padding: 0; }
  html, body {
    width: 1200px; height: 874px; overflow: hidden;
    background: var(--backdrop);
    font-family: "Questrial", "Century Gothic", sans-serif;
  }
  .canvas { position: relative; width: 1200px; height: 874px; }
  .card {
    position: absolute; top: 283px;
    width: 540px; height: 308px;
    background: var(--card-black);
    overflow: hidden;
    box-shadow: 0 14px 30px rgba(0,0,0,0.45);
  }
  .card--back { left: 40px; }
  .card--front { left: 620px; }

  /* front */
  .front-band {
    position: absolute; left: 0; right: 0; height: 52px;
    background: var(--brand-red);
  }
  .front-band--top { top: 0; border-bottom: 3px solid var(--brand-red-dark); }
  .front-band--bottom { bottom: 0; border-top: 3px solid var(--brand-red-dark); }
  .front-identity {
    position: absolute; left: 110px; top: 92px;
  }
  .wordmark {
    color: var(--text-light);
    font-size: 80px; line-height: 1; letter-spacing: 1px;
  }
  .company-name {
    color: var(--brand-red);
    font-size: 13px; letter-spacing: 4.2px; margin-top: 4px;
    white-space: nowrap;
  }
  .services {
    color: var(--text-light);
    font-size: 13px; letter-spacing: 0.5px; margin-top: 10px;
    text-align: right; padding-right: 4px; white-space: nowrap;
  }

  /* back */
  .contact {
    position: absolute; right: 30px; top: 44px;
    text-align: right; color: var(--text-light);
  }
  .contact-name { font-size: 21px; margin-bottom: 6px; }
  .contact-line { font-size: 13px; color: var(--text-muted); line-height: 1.5; }
  .back-band {
    position: absolute; left: 0; right: 0; top: 166px; height: 112px;
    background: var(--brand-red);
  }
  .back-identity { position: absolute; left: 28px; top: 20px; }
  .back-identity .wordmark { font-size: 60px; }
  .back-identity .company-name {
    color: var(--text-light); font-size: 9px; letter-spacing: 3.2px;
  }
</style>
</head>
<body>
<main class="canvas">
  <section class="card card--back" aria-label="Business card back">
    <div class="contact">
      <p class="contact-name">Marek Tollaway</p>
      <p class="contact-line">m: 0417295041</p>
      <p class="contact-line">e: kvora.holdings@mailbrook.example</p>
    </div>
    <div class="back-band">
      <div class="back-identity">
        <div class="wordmark">kvora</div>
        <p class="company-name">KVORA HOLDINGS PTY.LTD</p>
      </div>
    </div>
  </section>

  <section class="card card--front" aria-label="Business card front">
    <div class="front-band front-band--top"></div>
    <div class="front-identity">
      <div class="wordmark">kvora</div>
      <p class="company-name">KVORA HOLDINGS PTY.LTD</p>
      <p class="services">Domestic | Residential | Commercial</p>
    </div>
    <div class="front-band front-band--bottom"></div>
  </section>
</main>
</body>
</html>
```